Kelmora Legal Business Card

I require a corporate business card for a new legal services business.

I do not have a logo, nor do I want one.

I require a clean, neat a professional card for a law firm.

Details:

Business Name: Kelmora Legal
Name: Debra Lindqvist
Title: Corporate Services Manager
Location: Office 14 (Top Floor), Toravel Business Centre, Quinlan Grove Street, Alotau CBD, Milne Bay Province.
Postal Address: PO Box 593, Alotau, 211, Milne Bay Province, Papua New Guinea.
Contact: T: +675 6418250, F: +675 6413362, M: +675 72915867, E: dlindqvist@kelmoraexample.com.pg.

I look forward to your design submissions.

Industry/Entity Type

Legal

```html
<!DOCTYPE html>
<html lang="en">
<head>
<meta charset="utf-8">
<title>Kelmora Legal – Business Card</title>
<link rel="stylesheet" href="https://fonts.googleapis.com/css2?family=Roboto:ital,wght@0,300;0,400;0,500;0,700;1,400&display=swap">
<style>
  :root {
    --stage: #e6e6e4;
    --card: #ffffff;
    --teal: #6fbdb6;
    --teal-dark: #3f9f97;
    --band-edge: #4b4d4f;
    --ink: #3a3b3d;
    --ink-soft: #555759;
  }
  * { box-sizing: border-box; margin: 0; padding: 0; }
  html, body {
    width: 1200px; height: 747px; overflow: hidden;
    background: var(--stage);
    font-family: "Roboto", Arial, sans-serif;
    color: var(--ink);
  }
  .stage {
    width: 1200px; height: 747px;
    display: flex; align-items: center; justify-content: center;
  }
  .card {
    width: 400px; height: 660px;
    background: var(--card);
    box-shadow: 0 2px 10px rgba(0,0,0,0.12);
    display: flex; flex-direction: column;
  }
  .card-header {
    height: 150px;
    background: var(--teal);
    border-bottom: 9px solid var(--band-edge);
    display: flex; align-items: center; justify-content: center;
  }
  .brand-name {
    color: #ffffff;
    font-size: 40px;
    font-weight: 400;
    letter-spacing: 0.5px;
  }
  .card-body {
    flex: 1;
    padding: 52px 40px 40px;
    display: flex; flex-direction: column; align-items: center;
  }
  .person-name {
    font-size: 27px; font-weight: 700; color: var(--ink);
  }
  .person-title {
    margin-top: 4px;
    font-size: 14px; font-style: italic; color: var(--teal-dark);
  }
  .rule {
    width: 260px; height: 2px; background: var(--teal);
    margin: 24px 0;
  }
  .address {
    font-style: normal; text-align: center;
    font-size: 13.5px; line-height: 1.45; color: var(--ink-soft);
  }
  .address + .address { margin-top: 16px; }
  .contacts {
    align-self: flex-start;
    margin-top: 18px;
    list-style: none;
    font-size: 13.5px; line-height: 1.5; color: var(--ink-soft);
  }
  .contacts b { display: inline-block; width: 24px; font-weight: 700; color: var(--ink); }
</style>
</head>
<body>
<main class="stage">
  <article class="card">
    <header class="card-header">
      <span class="brand-name">Kelmora Legal</span>
    </header>
    <section class="card-body">
      <h1 class="person-name">Debra Lindqvist</h1>
      <p class="person-title">Corporate Services Manager</p>
      <div class="rule"></div>
      <address class="address">
        Office 14 (Top Floor)<br>
        Toravel Business Centre<br>
        Quinlan Grove Street, Alotau CBD, Milne Bay Province
      </address>
      <address class="address">
        PO Box 593, Alotau, 211,<br>
        Milne Bay Province, Papua New Guinea
      </address>
      <div class="rule"></div>
      <ul class="contacts">
        <li><b>T:</b>+675 6418250</li>
        <li><b>F:</b>+675 6413362</li>
        <li><b>M:</b>+675 72915867</li>
        <li><b>E:</b>dlindqvist@kelmoraexample.com.pg</li>
      </ul>
    </section>
  </article>
</main>
</body>
</html>
```